Women's Health Company needs business card

We need a business card for a USA based women's health care company. We use digital technology to enhance therapy prescribed by clinicians for their patients

```html
<!DOCTYPE html>
<html lang="en">
<head>
<meta charset="utf-8">
<title>Velora Health – Business Card</title>
<link href="https://fonts.googleapis.com/css2?family=Arimo:wght@400;700&display=swap" rel="stylesheet">
<style>
  :root {
    --stage: #b4b2ad;
    --card-black: #1b1b1b;
    --card-white: #ffffff;
    --teal: #74c1bd;
    --purple: #9457a6;
    --text-light: #e6e6e6;
    --emboss: #5a5a5a;
  }
  * { box-sizing: border-box; margin: 0; padding: 0; }
  html, body {
    width: 1200px; height: 857px; overflow: hidden;
    background: var(--stage);
    font-family: "Arimo", Arial, sans-serif;
  }
  .stage {
    position: relative; width: 1200px; height: 857px;
    display: flex; align-items: center; justify-content: center; gap: 48px;
  }
  .card {
    position: relative; width: 525px; height: 300px;
    background: var(--card-black);
    border-bottom: 3px solid var(--purple);
    border-left: 2px solid var(--purple);
    overflow: hidden;
  }
  .card-front__panel {
    position: absolute; inset: 0; width: 100%; height: 100%;
  }
  .brand {
    position: absolute; left: 40px; top: 72px;
    display: flex; align-items: center; gap: 10px;
  }
  .brand__dot {
    width: 14px; height: 14px; border-radius: 50%; background: var(--purple);
  }
  .brand__name {
    font-size: 34px; font-weight: 400; color: var(--teal); letter-spacing: 1px;
  }
  .holder { position: absolute; left: 40px; top: 150px; }
  .holder__name {
    font-size: 17px; font-weight: 700; color: var(--teal); letter-spacing: 0.5px;
  }
  .holder__role { font-size: 14px; color: var(--text-light); margin-top: 4px; }
  .contact-list {
    position: absolute; left: 40px; top: 208px; list-style: none;
  }
  .contact-list__item {
    display: flex; align-items: center; gap: 10px;
    font-size: 13px; color: var(--text-light); margin-bottom: 6px;
  }
  .contact-list__icon { width: 12px; height: 12px; flex: none; }
  .card-back { display: flex; align-items: center; justify-content: center; }
  .card-back__brand {
    font-size: 56px; font-weight: 400; color: var(--emboss); letter-spacing: 2px;
  }
</style>
</head>
<body>
<main class="stage">
  <section class="card card-front" aria-label="Business card front">
    <svg class="card-front__panel" viewBox="0 0 525 300" preserveAspectRatio="none" aria-hidden="true">
      <path d="M340 0 H525 V300 H380 C470 200 320 100 340 0 Z" fill="var(--card-white)"/>
    </svg>
    <div class="brand">
      <span class="brand__dot"></span>
      <span class="brand__name">Velora Health</span>
    </div>
    <div class="holder">
      <p class="holder__name">DANIEL REYES</p>
      <p class="holder__role">Operational Manager</p>
    </div>
    <ul class="contact-list">
      <li class="contact-list__item">
        <svg class="contact-list__icon" viewBox="0 0 12 12"><circle cx="6" cy="6" r="6" fill="var(--purple)"/><path d="M4 3.2 L5 4.6 L4.5 5.3 Q5.4 6.7 6.8 7.5 L7.4 7 L8.8 8 L8 9 Q5 8.5 3.2 4.2 Z" fill="var(--card-black)"/></svg>
        +1 555.210.4873
      </li>
      <li class="contact-list__item">
        <svg class="contact-list__icon" viewBox="0 0 12 12"><rect x="1" y="2.5" width="10" height="7" fill="var(--purple)"/><path d="M1 2.5 L6 6.5 L11 2.5" stroke="var(--card-black)" fill="none"/></svg>
        hello@velorahealth.example
      </li>
      <li class="contact-list__item">
        <svg class="contact-list__icon" viewBox="0 0 12 12"><circle cx="6" cy="6" r="5.5" fill="var(--purple)"/><path d="M0.5 6 H11.5 M6 0.5 V11.5 M6 0.5 Q2.5 6 6 11.5 M6 0.5 Q9.5 6 6 11.5" stroke="var(--card-black)" stroke-width="0.8" fill="none"/></svg>
        www.velorahealth.example
      </li>
    </ul>
  </section>

  <section class="card card-back" aria-label="Business card back">
    <span class="card-back__brand">Velora Health</span>
  </section>
</main>
</body>
</html>
```